Velqor5 Business Card - Health

Velqor5 maximizes value from the health data of its clients, including doctors, HMOs, and patients. I have attached the Velqor5 logo as an ai and eps file.
Target Market(s)
Health, HMO, Healthcare, Data, Big Data, Data Analytics
Industry/Entity Type
Business
Requirements
Must have
- At least one side should have some white on it so that we can write on it.

```html
<!DOCTYPE html>
<html lang="en">
<head>
<meta charset="utf-8">
<title>Velqor5 Business Card</title>
<link rel="stylesheet" href="https://fonts.googleapis.com/css2?family=Mulish:wght@400;700&display=swap">
<style>
  :root {
    --page-bg: #ecebe8;
    --card-bg: #ffffff;
    --brand-blue: #2a8fd4;
    --brand-blue-deep: #1e63b5;
    --ink: #232323;
    --on-blue: #ffffff;
  }
  * { margin: 0; padding: 0; box-sizing: border-box; }
  html, body {
    width: 1200px; height: 1000px; overflow: hidden;
    background: var(--page-bg);
    font-family: "Mulish", sans-serif;
  }
  .card {
    position: absolute;
    left: 265px;
    width: 665px;
    height: 397px;
    background: var(--card-bg);
    box-shadow: 0 3px 10px rgba(0,0,0,0.18);
    overflow: hidden;
  }
  .card--front { top: 73px; }
  .card--back { top: 533px; height: 396px; }

  .front-panel {
    position: absolute; left: 0; top: 0;
    width: 390px; height: 100%;
    background: linear-gradient(135deg, var(--brand-blue) 0%, #2b86cf 55%, var(--brand-blue-deep) 100%);
  }
  .contact {
    position: absolute; left: 38px; top: 72px;
    color: var(--on-blue);
  }
  .contact__name { font-weight: 700; font-size: 26px; line-height: 30px; }
  .contact__role { font-size: 19px; line-height: 24px; }
  .contact__address { margin-top: 34px; font-size: 19px; line-height: 24px; }
  .contact__list { list-style: none; margin-top: 16px; }
  .contact__item {
    display: flex; align-items: center; gap: 10px;
    font-size: 19px; height: 29px;
  }
  .contact__icon { width: 16px; height: 16px; flex: none; fill: none; stroke: var(--on-blue); stroke-width: 1.4; }

  .brand {
    position: absolute; left: 117px; top: 147px;
    display: flex; align-items: center; gap: 36px;
  }
  .brand__dot {
    width: 100px; height: 100px; border-radius: 50%;
    background: var(--brand-blue);
  }
  .brand__name {
    font-size: 84px; font-weight: 400; color: var(--ink);
    letter-spacing: -1px; line-height: 1;
  }
</style>
</head>
<body>
  <section class="card card--front">
    <div class="front-panel"></div>
    <div class="contact">
      <div class="contact__name">Marcus Ellery</div>
      <div class="contact__role">Manager</div>
      <div class="contact__address">418 Larkspur Ave 3rd floor<br>Fairmont, CA 94512</div>
      <ul class="contact__list">
        <li class="contact__item">
          <svg class="contact__icon" viewBox="0 0 16 16"><rect x="4.5" y="1" width="7" height="14" rx="1"/><line x1="6.5" y1="12.5" x2="9.5" y2="12.5"/></svg>
          + 555 010 204
        </li>
        <li class="contact__item">
          <svg class="contact__icon" viewBox="0 0 16 16"><path d="M1.5 6 Q8 1 14.5 6 L12.5 7.5 L10.5 6 L5.5 6 L3.5 7.5 Z"/><rect x="4" y="8.5" width="8" height="5.5" rx="1"/></svg>
          + 555 010 204
        </li>
        <li class="contact__item">
          <svg class="contact__icon" viewBox="0 0 16 16"><rect x="1.5" y="3.5" width="13" height="9"/><polyline points="1.5,3.5 8,9 14.5,3.5"/></svg>
          info@velqor5.com
        </li>
        <li class="contact__item">
          <svg class="contact__icon" viewBox="0 0 16 16"><circle cx="8" cy="8" r="6.5"/><ellipse cx="8" cy="8" rx="2.8" ry="6.5"/><line x1="1.5" y1="8" x2="14.5" y2="8"/></svg>
          www.velqor5.com
        </li>
      </ul>
    </div>
  </section>

  <section class="card card--back">
    <div class="brand">
      <div class="brand__dot"></div>
      <div class="brand__name">Velqor5</div>
    </div>
  </section>
</body>
</html>
```